Updated Business Cards

We need to update our business cards to reflect new services and employees. We are a luxury vacation rental company in Sandpoint, Idaho. Would also like to make the front facing font easier to read (larger fonts) I love the original logo created for our company and want to use this for the back of the business card created like before - with the dark blue color. See previous files.

Front of the card needs to include:
Employee Name
Title
Phone: 555-555-0147 (ext X)
Address: 417 W. Maple St, Ste 6
Harlow Bay, MT 83799
Book Direct: www.RestLakeview.example

```html
<!DOCTYPE html>
<html lang="en">
<head>
<meta charset="utf-8">
<title>Harlow Stays – Business Card</title>
<link href="https://fonts.googleapis.com/css2?family=Poppins:wght@400;500;600&display=swap" rel="stylesheet">
<style>
  :root {
    --page: #d9d1c4;
    --card: #ece8e1;
    --card-edge: #f7f4ef;
    --navy: #1b2558;
    --navy-light: #2d3b72;
    --slate: #4a4641;
    --band-text: #e4ddd2;
    --ink: #2a2825;
  }
  * { margin: 0; padding: 0; box-sizing: border-box; }
  html, body {
    width: 1200px; height: 1046px; overflow: hidden;
    background: var(--page);
    font-family: "Poppins", sans-serif;
  }
  .card {
    position: absolute; left: 152px; top: 292px;
    width: 945px; height: 514px;
    background: var(--card);
    border: 2px solid var(--card-edge);
    border-radius: 34px;
    overflow: hidden;
  }
  .brand {
    position: absolute; left: 0; right: 0; top: 86px;
    display: flex; justify-content: center; align-items: center; gap: 16px;
  }
  .brand-dot {
    width: 30px; height: 30px; border-radius: 50%; background: var(--navy);
  }
  .brand-name {
    font-weight: 600; font-size: 56px; line-height: 1;
    color: var(--navy); letter-spacing: 0.5px;
  }
  .info-band {
    position: absolute; left: 0; top: 308px; width: 945px; height: 122px;
  }
  .person {
    position: absolute; right: calc(945px - 414px); top: 322px;
    text-align: right; color: var(--band-text);
  }
  .person-name { font-size: 36px; line-height: 1.15; font-weight: 400; }
  .person-name strong { font-weight: 600; }
  .person-title { font-size: 20px; font-weight: 500; margin-top: 2px; }
  .contacts {
    position: absolute; left: 532px; top: 323px;
    list-style: none; color: var(--band-text);
  }
  .contacts li {
    display: flex; align-items: center; gap: 11px;
    font-size: 23px; line-height: 30px;
  }
  .contacts svg { width: 21px; height: 21px; flex: none; }
  .address {
    position: absolute; left: 0; right: 0; top: 446px;
    text-align: center; font-size: 22px; font-weight: 500; color: var(--ink);
  }
</style>
</head>
<body>
  <div class="card">
    <div class="brand">
      <span class="brand-dot"></span>
      <span class="brand-name">Harlow Stays</span>
    </div>

    <svg class="info-band" viewBox="0 0 945 122" aria-hidden="true">
      <defs>
        <linearGradient id="navyBand" x1="0" x2="1">
          <stop offset="0" stop-color="var(--navy)"/>
          <stop offset="0.75" stop-color="var(--navy-light)"/>
          <stop offset="1" stop-color="var(--navy)"/>
        </linearGradient>
      </defs>
      <polygon points="0,0 528,0 410,122 0,122" fill="url(#navyBand)"/>
      <polygon points="542,0 945,0 945,122 423,122" fill="var(--slate)"/>
    </svg>

    <div class="person">
      <div class="person-name"><strong>Marta</strong> Kolar</div>
      <div class="person-title">Founder &amp; CEO</div>
    </div>

    <ul class="contacts">
      <li>
        <svg viewBox="0 0 24 24" fill="none" stroke="currentColor" stroke-width="2" stroke-linecap="round" stroke-linejoin="round"><path d="M5 3h4l2 5-3 2a11 11 0 0 0 6 6l2-3 5 2v4a2 2 0 0 1-2 2A17 17 0 0 1 3 5a2 2 0 0 1 2-2z"/></svg>
        555-555-0147 (Ext X)
      </li>
      <li>
        <svg viewBox="0 0 24 24" fill="none" stroke="currentColor" stroke-width="2"><circle cx="12" cy="12" r="9"/><path d="M3 12h18M12 3c3 3 3 15 0 18M12 3c-3 3-3 15 0 18"/></svg>
        www.RestLakeview.example
      </li>
      <li>
        <svg viewBox="0 0 24 24" fill="none" stroke="currentColor" stroke-width="2" stroke-linejoin="round"><rect x="3" y="6" width="18" height="13" rx="1"/><path d="M3 7l9 7 9-7"/></svg>
        info@RestLakeview.example
      </li>
    </ul>

    <p class="address">417 W. Maple St, Ste 6, Harlow Bay, MT 83799</p>
  </div>
</body>
</html>
```